Natural Food Packaging - Peanut Butter bars

Name, branding, trade dress for new line of natural/organic peanut based protein bars. The concept its to package a high value natural product for mass consumer consumption.

There will be 2 to 4 flavors initially introduced. Each flavor has a printed film wrapper and shelf display box. The design winner will have first preference for all the packaging work.Think peanut butter chocolate chip, peanut butter with cranberries, coconut, etc.

We are a privately owned, internationally established organic food manufacturer.

This will be a high profile, well recognized project within the industry.

It is an excellent opportunity for a long term business relationship.

Halvey Market(s)

consumers who want a better quality protein bar than they currently buy. Mostly active adults age 18-50

Industry/Entity Type

Business

Requirements
Must have
• A product name/brand and general look and feel. It needs to convey purity, great ingredients/quality, taste and great price.

It needs to have mass appeal...think Halvey and 4-22, not just Brindlecrest Market.
Nice to have
• Package mock up images for 2 or 3 flavors

```html
<!DOCTYPE html>
<html lang="en">
<head>
<meta charset="utf-8">
<title>Peanova – Peanut Butter Nutrition Bars</title>
<link rel="stylesheet" href="https://fonts.googleapis.com/css2?family=Tinos:wght@400;700&display=swap">
<style>
  :root {
    --stage: #000000;
    --film: #ffffff;
    --film-shade: #e9e9e9;
    --crimp-line: #d2d2d2;
    --cocoa: #5a2f1a;
    --caramel: #c8702a;
    --toffee: #8a5a2b;
    --berry: #b0307a;
    --honey: #a8782a;
    --plum: #7a2a4a;
    --leaf: #6cbf3a;
    --bar-dark: #4a2414;
    --bar-light: #8a4a2a;
  }
  * { box-sizing: border-box; margin: 0; padding: 0; }
  html, body { width: 1200px; height: 1200px; overflow: hidden; background: var(--stage); }
  body { font-family: "Tinos", "Times New Roman", serif; }

  .shelf {
    width: 1200px; height: 1200px;
    display: flex; flex-direction: column; justify-content: center; gap: 44px;
    padding: 0 50px;
  }

  .wrapper {
    position: relative; width: 1100px; height: 320px;
    display: flex;
    filter: drop-shadow(0 4px 10px rgba(255,255,255,0.08));
  }
  .crimp {
    width: 46px; height: 100%;
    background:
      repeating-linear-gradient(90deg, var(--film) 0 5px, var(--crimp-line) 5px 6px);
  }
  .crimp--left  { clip-path: polygon(0 0, 100% 0, 100% 100%, 0 100%, 12px 97.5%, 0 95%, 12px 92.5%, 0 90%, 12px 87.5%, 0 85%, 12px 82.5%, 0 80%, 12px 77.5%, 0 75%, 12px 72.5%, 0 70%, 12px 67.5%, 0 65%, 12px 62.5%, 0 60%, 12px 57.5%, 0 55%, 12px 52.5%, 0 50%, 12px 47.5%, 0 45%, 12px 42.5%, 0 40%, 12px 37.5%, 0 35%, 12px 32.5%, 0 30%, 12px 27.5%, 0 25%, 12px 22.5%, 0 20%, 12px 17.5%, 0 15%, 12px 12.5%, 0 10%, 12px 7.5%, 0 5%, 12px 2.5%); }
  .crimp--right { clip-path: polygon(0 0, 100% 0, calc(100% - 12px) 2.5%, 100% 5%, calc(100% - 12px) 7.5%, 100% 10%, calc(100% - 12px) 12.5%, 100% 15%, calc(100% - 12px) 17.5%, 100% 20%, calc(100% - 12px) 22.5%, 100% 25%, calc(100% - 12px) 27.5%, 100% 30%, calc(100% - 12px) 32.5%, 100% 35%, calc(100% - 12px) 37.5%, 100% 40%, calc(100% - 12px) 42.5%, 100% 45%, calc(100% - 12px) 47.5%, 100% 50%, calc(100% - 12px) 52.5%, 100% 55%, calc(100% - 12px) 57.5%, 100% 60%, calc(100% - 12px) 62.5%, 100% 65%, calc(100% - 12px) 67.5%, 100% 70%, calc(100% - 12px) 72.5%, 100% 75%, calc(100% - 12px) 77.5%, 100% 80%, calc(100% - 12px) 82.5%, 100% 85%, calc(100% - 12px) 87.5%, 100% 90%, calc(100% - 12px) 92.5%, 100% 95%, calc(100% - 12px) 97.5%, 100% 100%, 0 100%); }

  .panel {
    flex: 1; position: relative; display: flex;
    background: linear-gradient(180deg, var(--film) 0%, var(--film) 70%, var(--film-shade) 100%);
    border-left: 2px solid var(--crimp-line);
    border-right: 2px solid var(--crimp-line);
  }

  .front { position: relative; width: 560px; height: 100%; }
  .product-shot {
    position: absolute; left: 24px; bottom: 22px; width: 260px; height: 92px;
    border-radius: 18px;
    background: linear-gradient(170deg, var(--bar-light), var(--bar-dark));
  }
  .ingredient-art {
    position: absolute; left: 400px; top: 28px; width: 96px; height: 56px;
    border-radius: 28px;
    background: linear-gradient(120deg, var(--caramel), #e9b07a);
  }
  .ingredient-art--berry { background: linear-gradient(120deg, var(--caramel), #c0282e); }
  .ingredient-art--chip  { background: linear-gradient(120deg, var(--cocoa), #e2c08a); }

  .brand-name {
    position: absolute; left: 24px; top: 92px;
    font-weight: 700; font-size: 112px; line-height: 1; letter-spacing: -2px;
    color: var(--cocoa);
  }
  .flavour {
    position: absolute; left: 300px; top: 222px;
    font-size: 22px; color: var(--toffee);
  }
  .flavour--berry { color: var(--berry); }

  .bands { flex: 1; display: flex; position: relative; }
  .band { height: 100%; }
  .band--caramel { width: 24%; background: var(--caramel); }
  .band--toffee  { width: 24%; background: var(--toffee); }
  .band--berry   { width: 28%; background: var(--berry); }
  .band--honey   { width: 24%; background: var(--honey); }

  .seal {
    position: absolute; left: -34px; top: 26px; width: 62px; height: 62px;
    border-radius: 50%; background: var(--leaf); border: 3px solid var(--film);
  }

  .label {
    position: absolute; left: 49%; top: 110px; width: 160px; padding: 12px 14px;
    background: var(--plum); color: var(--film); text-align: center;
    line-height: 1.1;
  }
  .label__claim { font-size: 22px; border-bottom: 1px solid var(--film); display: inline-block; }
  .label__type  { font-size: 16px; margin-bottom: 8px; }
  .label__net   { font-size: 20px; }
</style>
</head>
<body>
<main class="shelf">

  <article class="wrapper" aria-label="Peanut butter with coconut wrapper">
    <div class="crimp crimp--left"></div>
    <div class="panel">
      <div class="front">
        <div class="ingredient-art" role="img" aria-label="Illustration of peanuts and coconut pieces"></div>
        <div class="brand-name">Peanova</div>
        <p class="flavour">peanut butter with coconut</p>
        <div class="product-shot" role="img" aria-label="Photo of a chocolate-coated peanut bar"></div>
      </div>
      <div class="bands">
        <div class="seal" aria-hidden="true"></div>
        <div class="band band--caramel"></div>
        <div class="band band--toffee"></div>
        <div class="band band--berry"></div>
        <div class="band band--honey"></div>
        <div class="label">
          <div class="label__claim">all-natural</div>
          <div class="label__type">nutrition bars</div>
          <div class="label__net">NET 1.76<br>OZ (50g)</div>
        </div>
      </div>
    </div>
    <div class="crimp crimp--right"></div>
  </article>

  <article class="wrapper" aria-label="Peanut butter chocolate chip wrapper">
    <div class="crimp crimp--left"></div>
    <div class="panel">
      <div class="front">
        <div class="ingredient-art ingredient-art--chip" role="img" aria-label="Illustration of chocolate chips and peanuts"></div>
        <div class="brand-name">Peanova</div>
        <p class="flavour">peanut butter chocolate chip</p>
        <div class="product-shot" role="img" aria-label="Photo of a chocolate-coated peanut bar"></div>
      </div>
      <div class="bands">
        <div class="seal" aria-hidden="true"></div>
        <div class="band band--caramel"></div>
        <div class="band band--toffee"></div>
        <div class="band band--berry"></div>
        <div class="band band--honey"></div>
        <div class="label">
          <div class="label__claim">all-natural</div>
          <div class="label__type">nutrition bars</div>
          <div class="label__net">NET 1.76<br>OZ (50g)</div>
        </div>
      </div>
    </div>
    <div class="crimp crimp--right"></div>
  </article>

  <article class="wrapper" aria-label="Peanut butter with cranberries wrapper">
    <div class="crimp crimp--left"></div>
    <div class="panel">
      <div class="front">
        <div class="ingredient-art ingredient-art--berry" role="img" aria-label="Illustration of peanuts and cranberries"></div>
        <div class="brand-name">Peanova</div>
        <p class="flavour flavour--berry">peanut butter with cranberries</p>
        <div class="product-shot" role="img" aria-label="Photo of a chocolate-coated peanut bar with cranberries"></div>
      </div>
      <div class="bands">
        <div class="seal" aria-hidden="true"></div>
        <div class="band band--caramel"></div>
        <div class="band band--toffee"></div>
        <div class="band band--berry"></div>
        <div class="band band--honey"></div>
        <div class="label">
          <div class="label__claim">all-natural</div>
          <div class="label__type">nutrition bars</div>
          <div class="label__net">NET 1.76<br>OZ (50g)</div>
        </div>
      </div>
    </div>
    <div class="crimp crimp--right"></div>
  </article>

</main>
</body>
</html>
```